IT Company based on Biology Business Needs a Business Card Design

We need a business card design for a new company called 'Lumen CELL'. We develop the machine learning solutions especially focused on deep learning algorithms for biology industry. Our initial product is a vision detection on biological images to help doctors diagnose the symptoms. We would like to see designs that use the color green.

Industry/Entity Type

Business

```html
<!DOCTYPE html>
<html lang="en">
<head>
<meta charset="utf-8">
<title>Lumen CELL – Business Card</title>
<link rel="stylesheet" href="https://fonts.googleapis.com/css2?family=Open+Sans:wght@400;600;700&display=swap">
<style>
  :root {
    --backdrop: #6e4a33;
    --card: #1f1f1f;
    --green-bright: #7dc242;
    --green-deep: #2e9e48;
    --green-mid: #3aa94c;
    --green-light: #8cc63f;
  }
  * { margin: 0; padding: 0; box-sizing: border-box; }
  html, body {
    width: 1200px;
    height: 1000px;
    overflow: hidden;
    background: var(--backdrop);
    font-family: "Open Sans", Arial, sans-serif;
  }
  .canvas { position: relative; width: 1200px; height: 1000px; }

  .card {
    position: absolute;
    left: 265px;
    width: 666px;
    height: 397px;
    background: var(--card);
    border-radius: 24px;
    overflow: hidden;
  }
  .card--front { top: 73px; }
  .card--back  { top: 532px; }

  .brand {
    position: absolute;
    display: flex;
    align-items: center;
    color: var(--green-bright);
    font-weight: 600;
    letter-spacing: -0.04em;
    text-transform: uppercase;
    white-space: nowrap;
    line-height: 1;
  }
  .brand__dot {
    border-radius: 50%;
    background: var(--green-bright);
    flex: none;
  }
  .card--front .brand { left: 140px; top: 162px; font-size: 60px; }
  .card--front .brand__dot { width: 40px; height: 40px; margin-right: 18px; }
  .card--back .brand { left: 46px; top: 176px; font-size: 44px; }
  .card--back .brand__dot { width: 28px; height: 28px; margin-right: 14px; }

  .contact {
    position: absolute;
    left: 413px;
    top: 76px;
    color: var(--green-mid);
  }
  .contact__name {
    font-size: 20px;
    font-weight: 700;
    letter-spacing: 0.03em;
    color: var(--green-mid);
    line-height: 26px;
  }
  .contact__role {
    font-size: 16px;
    color: var(--green-light);
    line-height: 22px;
  }
  .contact__address {
    margin-top: 42px;
    font-size: 15px;
    line-height: 22px;
    font-style: normal;
  }
  .contact__lines {
    list-style: none;
    margin-top: 16px;
    font-size: 16px;
    line-height: 24px;
    color: var(--green-light);
  }
  .contact__lines li { display: flex; align-items: center; }
  .contact__lines svg {
    width: 15px; height: 15px;
    margin-right: 9px;
    fill: var(--green-mid);
    flex: none;
  }
</style>
</head>
<body>
<main class="canvas">

  <section class="card card--front" aria-label="Card front">
    <div class="brand"><span class="brand__dot"></span>Lumen CELL</div>
  </section>

  <section class="card card--back" aria-label="Card back">
    <div class="brand"><span class="brand__dot"></span>Lumen CELL</div>

    <div class="contact">
      <p class="contact__name">MARA ELLISON</p>
      <p class="contact__role">Manager</p>
      <address class="contact__address">
        218 Fernhill Avenue,<br>
        Suite 40<br>
        Dalton, GA 30720
      </address>
      <ul class="contact__lines">
        <li>
          <svg viewBox="0 0 16 16" aria-hidden="true"><path d="M3 2h3l1.5 3.5-2 1.2a8 8 0 0 0 3.8 3.8l1.2-2L14 10v3a1 1 0 0 1-1 1A11 11 0 0 1 2 3a1 1 0 0 1 1-1z"/></svg>
          555 014 2290
        </li>
        <li>
          <svg viewBox="0 0 16 16" aria-hidden="true"><path d="M1 3h14v10H1z M2 4.2v.6l6 4 6-4v-.6z" fill-rule="evenodd"/></svg>
          hello@lumencell.com
        </li>
        <li>
          <svg viewBox="0 0 16 16" aria-hidden="true"><circle cx="8" cy="8" r="6.5" fill="none" stroke="currentColor" stroke-width="1.5" style="stroke: var(--green-mid)"/><path d="M1.5 8h13M8 1.5c-2.5 3-2.5 10 0 13M8 1.5c2.5 3 2.5 10 0 13" fill="none" style="stroke: var(--green-mid)" stroke-width="1.2"/></svg>
          www.lumencell.com
        </li>
      </ul>
    </div>
  </section>

</main>
</body>
</html>
```